PROPERTY MANAGEMENT AND REAL ESTATE

Target Market(s)

real estate owners and investors

Industry/Entity Type

Real Estate

Contact Information for Business Card

BRIGHT LANTERN PROPERTY MANAGEMENT GROUP, LLC
487 North Corwin Parkway
Suite 260
Marlow Springs, FL 33127

```html
<!DOCTYPE html>
<html lang="en">
<head>
<meta charset="utf-8">
<title>Bright Lantern Property Management Group – Business Card</title>
<link rel="stylesheet" href="https://fonts.googleapis.com/css2?family=Montserrat:wght@300;600&display=swap">
<style>
  :root {
    --backdrop: #e6e9e9;
    --card-white: #ffffff;
    --maroon: #5e0000;
    --maroon-bright: #8c0a0a;
    --ink: #1a1a1a;
  }
  html, body {
    margin: 0;
    width: 1200px;
    height: 704px;
    overflow: hidden;
    background: var(--backdrop);
  }
  .sheet {
    position: relative;
    width: 1200px;
    height: 704px;
    box-sizing: border-box;
    padding-top: 52px;
    display: flex;
    justify-content: center;
    align-items: flex-start;
    gap: 14px;
  }
  .card {
    position: relative;
    width: 532px;
    height: 312px;
    overflow: hidden;
    font-family: "Montserrat", Arial, sans-serif;
  }
  .card--front { background: var(--card-white); }
  .card--back { background: var(--maroon); }

  .corner-pattern {
    position: absolute;
    top: 0;
    right: 0;
    width: 150px;
    height: 312px;
  }

  .brand {
    position: absolute;
    display: flex;
    align-items: center;
    gap: 10px;
    font-weight: 600;
    font-size: 15px;
    letter-spacing: 0.12em;
    white-space: nowrap;
  }
  .brand__dot {
    width: 34px;
    height: 34px;
    border-radius: 50%;
  }
  .card--front .brand {
    left: 49%;
    top: 92px;
    transform: translate(-50%, -50%);
    color: var(--maroon-bright);
  }
  .card--front .brand__dot { background: var(--maroon-bright); }
  .card--back .brand {
    left: 50%;
    top: 50%;
    transform: translate(-50%, -50%);
    color: var(--card-white);
  }
  .card--back .brand__dot { background: var(--card-white); }

  .company-name {
    position: absolute;
    left: 160px;
    top: 160px;
    margin: 0;
    font-weight: 300;
    font-size: 15px;
    line-height: 1.35;
    letter-spacing: 0.02em;
    color: var(--ink);
  }
  .contact {
    position: absolute;
    left: 0;
    width: 98%;
    top: 271px;
    margin: 0;
    text-align: center;
    font-style: normal;
    font-weight: 600;
    font-size: 11.5px;
    line-height: 1.55;
    color: var(--ink);
  }
</style>
</head>
<body>
<main class="sheet">
  <section class="card card--front" aria-label="Business card front">
    <svg class="corner-pattern" viewBox="0 0 150 312" role="img" aria-label="Maroon dotted pattern sweeping down the right edge">
      <path d="M150 0 H38 C70 18 92 40 104 70 C116 100 118 140 124 180 C128 220 132 260 138 312 H150 Z" fill="var(--maroon)" opacity="0.85"/>
      <rect x="142" y="0" width="8" height="312" fill="var(--maroon)"/>
    </svg>
    <div class="brand"><span class="brand__dot"></span>BRIGHT LANTERN</div>
    <h1 class="company-name">BRIGHT LANTERN PROPERTY<br>MANAGEMENT GROUP, LLC</h1>
    <address class="contact">
      487 North Corwin Parkway Suite 260 Marlow Springs, FL 33127<br>
      Phone: 555-201-0148 Fax: 555-201-0193
    </address>
  </section>

  <section class="card card--back" aria-label="Business card back">
    <div class="brand"><span class="brand__dot"></span>BRIGHT LANTERN</div>
  </section>
</main>
</body>
</html>
```